Executive retreat/workshop flyer for Harbor Pathway

Our company, Harbor Pathway, runs intensive week long residential retreats for executives suffering from burnout syndrome. We have a programme of therapy which will enable clients to get clarity on what they want out of life and how to achieve it.

Our website is www.harborpathway-example.com. The flyer should have a consistent look and feel to the website. The flyer should be suitable for electronic distribution as well as printing.

The copy should read:

What is it all for? (IN BIG BOLD FONT)

We invite you to The Harbor Pathway

Discover a more meaningful way of being in this world and put passion and purpose back into your life.

Our leading experts will guide you through a holistic program of intellectual, physical, emotional, spiritual and financial work.

You will:

- Draw up a vision of how you want to live your life
- Understand negative behavior loops and how to manage them
- Rebalance relationships which have suffered from stress and neglect
- Examine your attitudes towards money through the Quadrafold System
- Access practical advice on how to implement your goals

Please join us in the beautiful Castlereagh Peninsula this August for a life-changing journey.

This is an intensive program custom tailored to your individual needs. We can only take on a very limited number of participants to maintain intimacy and quality of attention. Book early to avoid disappointment.

Details:

date - mon 27 August - sat 1 sept 2012

Venue- kestrelwood Eco retreat, stony ford, Australia, 1 hour from Melbourne

Price- Special launch offer of US$ 13,860 which is a 30% discount off the normal price of US$ 19,800

10% of profits go to charity

All accommodation, food and individual consultations included.

Please email info@harborpathway-example.com or contact Marnie at 6031 2946

Target Market(s)

Senior executives and leaders mostly with a financial background.

Industry/Entity Type

Residential

Requirements
Must have
• The brochure should look clear in electronic and print format. Can use photos which I've attached.
Nice to have
• Should have a warm, serene feel but appear professional and reliable.

```html
<!DOCTYPE html>
<html lang="en">
<head>
<meta charset="utf-8">
<title>Harbor Pathway – Retreat Flyer</title>
<link rel="stylesheet" href="https://fonts.googleapis.com/css2?family=Cinzel:wght@700&family=Arimo:ital,wght@0,400;0,700;1,400&display=swap">
<style>
  :root {
    --page-bg: #eef1ea;
    --paper: #ffffff;
    --plum: #5a1a5e;
    --olive: #7f8f14;
    --lilac: #a88bbd;
    --rule: #b7a6c6;
    --ink: #1a1a1a;
    --title-band: #dfe6cf;
    --leaf-dark: #3d4a2a;
    --leaf-warm: #b8742c;
    --leaf-light: #e7d7a0;
  }
  * { box-sizing: border-box; margin: 0; padding: 0; }
  html, body { width: 1200px; height: 900px; overflow: hidden; }
  body {
    background: var(--page-bg);
    font-family: "Arimo", Arial, sans-serif;
    color: var(--ink);
    position: relative;
  }
  .flyer {
    position: absolute; left: 335px; top: 22px;
    width: 550px; height: 778px;
    background: var(--paper);
    box-shadow: 0 4px 18px rgba(0,0,0,.12);
  }
  .photo-band {
    position: absolute; left: 0; width: 100%;
    background: linear-gradient(100deg, var(--leaf-dark) 0%, var(--leaf-warm) 30%, var(--leaf-light) 55%, var(--leaf-warm) 75%, var(--leaf-dark) 100%);
  }
  .photo-band--top { top: 0; height: 93px; }
  .photo-band--bottom { bottom: 0; height: 32px; }
  .title-band {
    position: absolute; top: 93px; left: 0; width: 100%; height: 88px;
    background: linear-gradient(180deg, #e6ebd9, var(--title-band));
    border-bottom: 1px solid var(--rule);
    display: flex; align-items: center; justify-content: center;
  }
  .headline {
    font-family: "Cinzel", "Times New Roman", serif;
    font-weight: 700; font-size: 50px; color: var(--plum);
    letter-spacing: .5px;
  }
  .tab {
    position: absolute; left: 230px; width: 91px; height: 16px;
    background: var(--lilac); color: #fff;
    font-size: 12px; line-height: 16px; text-align: center;
  }
  .tab--invite { top: 182px; }
  .tab--details { top: 595px; }
  .brand {
    position: absolute; top: 238px; left: 0; width: 100%;
    display: flex; flex-direction: column; align-items: center; gap: 10px;
  }
  .brand__dot { width: 34px; height: 34px; border-radius: 50%; background: var(--plum); }
  .brand__name {
    font-family: "Cinzel", "Times New Roman", serif; font-weight: 700;
    font-size: 23px; color: var(--plum);
  }
  .col { position: absolute; top: 323px; }
  .col--left { left: 34px; width: 222px; }
  .col--right { left: 293px; width: 240px; top: 324px; }
  .lead { color: var(--olive); font-weight: 700; font-size: 13px; line-height: 17px; }
  .body-copy { font-size: 13px; line-height: 16px; margin-top: 14px; }
  .body-copy--small { font-size: 11px; line-height: 17px; margin-top: 12px; }
  .subhead { color: var(--olive); font-weight: 700; font-size: 15px; margin-top: 18px; }
  .benefits { list-style: none; margin-top: 3px; }
  .benefits li {
    position: relative; padding-left: 11px;
    font-size: 11px; line-height: 16px; margin-bottom: 3px;
  }
  .benefits svg { position: absolute; left: 0; top: 3px; width: 9px; height: 9px; }
  .col--right .benefits li { padding-left: 14px; }
  .col--right .lead { margin-top: 26px; line-height: 19px; }
  .details-rule {
    position: absolute; top: 595px; left: 0; width: 100%;
    border-top: 1px solid var(--rule);
  }
  .detail { position: absolute; font-style: italic; }
  .detail dt { color: var(--plum); font-size: 13px; line-height: 16px; }
  .detail dd { font-size: 12.5px; line-height: 15px; margin-bottom: 4px; }
  .detail--left { left: 34px; top: 622px; width: 240px; }
  .detail--right { left: 294px; top: 622px; width: 240px; }
  .footer-note {
    position: absolute; top: 713px; left: 0; width: 100%;
    text-align: center; font-size: 10.5px; line-height: 15px;
  }
</style>
</head>
<body>
  <main class="flyer">
    <div class="photo-band photo-band--top" role="img" aria-label="Sunlit autumn vine leaves"></div>
    <header class="title-band"><h1 class="headline">What is it all for?</h1></header>
    <div class="tab tab--invite">We invite you to:</div>

    <div class="brand">
      <span class="brand__dot"></span>
      <span class="brand__name">The Harbor Pathway</span>
    </div>

    <section class="col col--left">
      <p class="lead">Discover a more meaningful way of being in this world and put passion and purpose back into your life.</p>
      <p class="body-copy">Our leading experts will guide you through a holistic program of intellec-tual, physical, emotional, spiritual and financial work.</p>
      <h2 class="subhead">You will:</h2>
      <ul class="benefits">
        <li><svg viewBox="0 0 10 10"><path d="M1 6 L4 9 L9 1" fill="none" stroke="#7f8f14" stroke-width="2"/></svg>Draw up a vision of how you want to live your life</li>
        <li><svg viewBox="0 0 10 10"><path d="M1 6 L4 9 L9 1" fill="none" stroke="#7f8f14" stroke-width="2"/></svg>Understand negative behavior loops and how to manage them</li>
        <li><svg viewBox="0 0 10 10"><path d="M1 6 L4 9 L9 1" fill="none" stroke="#7f8f14" stroke-width="2"/></svg>Rebalance relationships which have suffered from stress and neglect</li>
      </ul>
    </section>

    <section class="col col--right">
      <ul class="benefits">
        <li><svg viewBox="0 0 10 10"><path d="M1 6 L4 9 L9 1" fill="none" stroke="#7f8f14" stroke-width="2"/></svg>Examine your attitudes towards money through the Quadrafold System</li>
        <li><svg viewBox="0 0 10 10"><path d="M1 6 L4 9 L9 1" fill="none" stroke="#7f8f14" stroke-width="2"/></svg>Access practical advice on how to implement your goals</li>
      </ul>
      <p class="lead">Please join us in the beautiful Castlereagh Peninsula this August for a life-changing journey.</p>
      <p class="body-copy body-copy--small">This is an intensive program custom tailored to your individual needs. We can only take on a very limited number of participants to maintain intimacy and quality of attention. Book early to avoid disappointment.</p>
    </section>

    <div class="details-rule"></div>
    <div class="tab tab--details">Details</div>

    <dl class="detail detail--left">
      <dt>Date:</dt>
      <dd>Mon 27 August - Sat 1 sept 2012</dd>
      <dt>Venue:</dt>
      <dd>Kestrelwood Eco Retreat, Stony Ford, Australia, 1 hour from Melbourne</dd>
    </dl>
    <dl class="detail detail--right">
      <dt>Price:</dt>
      <dd>Special launch offer of US$ 13,860 which is a 30% discount off the normal price of US$ 19,800 10% of profits go to charity</dd>
    </dl>

    <p class="footer-note">All accommodation, food and individual consultations included.<br>Please email info@harborpathway-example.com or contact Marnie at 6031 2946</p>

    <div class="photo-band photo-band--bottom" role="img" aria-label="Strip of sunlit autumn vine leaves"></div>
  </main>
</body>
</html>
```